"Velvet Ember" sexual performance enhancement pill bottle label needed.

This should be interesting...

I am starting a line of sexual performance enhancement products. This will be the first of several products basically. Keep in mind, I am the type of business person to stay with one company for years if they provide me with quality work.

This particular product is a male sexual performance pill. The name of the product is "Velvet Ember." The packaging of the pills are a black bottle with a white top. Label on the product example would be perfect but at a minimum I have attached a "template" for your guidance.

Some of the technical aspects of this are as follows:

-File Format: Illustrator CS6 is preferred. (Winner must provide artwork in layer and can not flatten artwork.)
-Resolution: 300 dpi minimum
-Bleed: 1/16th (0.0625") inch from edge of label
-Color Mode: CMYK only or must be converted to CMYK for final production

Lastly, this is your project as a designer, artist, creator, this is essentially a piece of you that will be sold and known by thousands of people. I have no color scheme that I prefer, just use the template and follow the layout. If you have any further questions, please feel free to contact me at any time.
Updates

Quick note on the product and what it does: -Powerful, long lasting, harder erections -Works in a minutes and last for hours -Enhances sexual desire and drive Thank you for your ideas...

Project Deadline Extended
Reason: We decided to extent the project for a few more days to let the last few concepts come in. So far things are looking really good and we definitely have seen some amazing designs. Thank you for your hard work and amazing creativity. Looking forward to seeing what we have come in the next couple of day. Very respectfully, Doran

ONLY THREE DAYS LEFT!!!! Please submit your ideas as soon as possible. And as always, thank you for your help!!! V/r, Doran

Industry/Entity Type

Graphic Design

```html
<!DOCTYPE html>
<html lang="en">
<head>
<meta charset="utf-8">
<title>Velvet Ember – Bottle Label</title>
<link rel="stylesheet" href="https://fonts.googleapis.com/css2?family=Anton&family=Roboto+Condensed:wght@400;700&family=Oswald:wght@500;700&display=swap">
<style>
  :root {
    --canvas: #ffffff;
    --label-black: #000000;
    --brand-red: #ff1a0a;
    --ink-white: #ffffff;
  }
  * { box-sizing: border-box; margin: 0; padding: 0; }
  html, body { width: 1200px; height: 1001px; overflow: hidden; background: var(--canvas); }
  .label {
    position: absolute; left: 41px; top: 281px;
    width: 822px; height: 322px;
    background: var(--label-black);
    transform: scale(1.36); transform-origin: top left;
    color: var(--ink-white);
    font-family: "Roboto Condensed", sans-serif;
  }
  .usage { position: absolute; left: 30px; top: 47px; width: 232px; font-size: 7.1px; line-height: 1.22; font-weight: 700; text-align: justify; }
  .usage .lead { color: var(--brand-red); }
  .usage .warning { color: var(--brand-red); margin-top: 6px; }
  .fda-note { margin-top: 7px; border: 1.5px solid var(--ink-white); padding: 4px 6px; font-size: 6.4px; line-height: 1.3; }
  .maker { position: absolute; left: 30px; top: 254px; display: flex; gap: 8px; font-size: 4.6px; font-weight: 700; line-height: 1.4; }
  .maker .mini-name { font-family: "Anton", sans-serif; color: var(--brand-red); font-size: 7px; line-height: 0.95; margin-top: 7px; width: 26px; }
  .maker .web { color: var(--brand-red); letter-spacing: 0.8px; }
  .brand { position: absolute; left: 290px; top: 46px; width: 260px; text-align: center; font-family: "Anton", sans-serif; color: var(--brand-red); font-size: 62px; line-height: 1.0; letter-spacing: 1px; }
  .claim { position: absolute; top: 203px; font-family: "Oswald", sans-serif; font-weight: 500; font-size: 11.5px; }
  .claim.count { left: 337px; }
  .claim.pure { left: 425px; }
  .strength { position: absolute; left: 291px; top: 246px; width: 257px; height: 30px; }
  .strength .bar { position: absolute; left: 35px; top: 0; width: 187px; height: 30px; background: var(--brand-red); font-family: "Oswald", sans-serif; font-weight: 700; font-size: 19px; line-height: 30px; text-align: center; }
  .dietary { position: absolute; left: 290px; top: 289px; width: 260px; text-align: center; font-family: "Oswald", sans-serif; font-weight: 500; font-size: 11px; }
  .facts { position: absolute; left: 583px; top: 47px; width: 204px; height: 197px; border: 2px solid var(--ink-white); padding: 7px 8px; }
  .facts h2 { font-family: "Oswald", sans-serif; font-weight: 700; color: var(--brand-red); font-size: 18px; line-height: 1.1; }
  .facts p { font-size: 8.6px; line-height: 1.25; }
  .rule { height: 4px; background: var(--ink-white); margin: 4px 0; }
  .rule.thin { height: 2px; }
  .facts .amount { display: flex; justify-content: space-between; font-size: 8.4px; }
  .facts .formula { color: var(--brand-red); font-weight: 700; font-size: 8.4px; }
  .facts .ingredients { font-size: 6.7px; line-height: 1.3; font-weight: 700; }
  .facts .dv { font-weight: 700; font-size: 9.5px; }
  .other { position: absolute; left: 591px; top: 252px; width: 200px; font-size: 6.9px; line-height: 1.4; font-weight: 700; }
  .other span { color: var(--brand-red); }
</style>
</head>
<body>
<main class="label">
  <section class="usage">
    <p><span class="lead">SUGGESTED USE:</span> As a dietary supplement, take two (2) capsules 1 hour before physical activity, or as directed by your health care professional. Do not exceed two (2) capsules daily. <span class="lead">CAUTION:</span> Do not exceed recommended dose. This product is not intended for pregnant or nursing mothers, children under the age of 18, or individuals taking prescription drugs. Discontinue use immediately if nausea, sleeplessness, or nervousness occur. Do not take this product if you have a known medical condition including high blood pressure, diabetes, any cardiovascular disorder, heart disease, hyperthyroidism, or are taking anti-depressant medications. If you have questions about the advisability of taking this product, consult your physician prior to use.</p>
    <p class="warning">KEEP OUT OF THE REACH OF CHILDREN. DO NOT USE IF SAFETY SEAL IS DAMAGED OR MISSING. STORE AT ROOM TEMPERATURE.</p>
    <p class="fda-note">* These statements have not been evaluated by the Food and Drug Administration. This product is not intended to diagnose, treat, cure or prevent any disease.</p>
  </section>
  <footer class="maker">
    <div class="mini-name">VELVET EMBER</div>
    <div>
      <p>Manufactured Exclusively For:</p>
      <p>1187 Harlow St. Millbrook, OH</p>
      <p>P: 555.201.0178 &nbsp; F: 555.201.0190</p>
      <p class="web">www.velvetemberpill.com</p>
    </div>
  </footer>

  <h1 class="brand">VELVET<br>EMBER</h1>
  <p class="claim count">1600</p>
  <p class="claim pure">PURE AND POTENT*</p>
  <div class="strength">
    <svg width="257" height="30" aria-hidden="true">
      <g fill="#ff1a0a">
        <rect x="0" y="0" width="4" height="30"/><rect x="9" y="0" width="4" height="30"/><rect x="18" y="0" width="8" height="30"/>
        <rect x="231" y="0" width="8" height="30"/><rect x="244" y="0" width="4" height="30"/><rect x="253" y="0" width="4" height="30"/>
      </g>
    </svg>
    <div class="bar">MAX STRENGTH!</div>
  </div>
  <p class="dietary">DIETARY SUPPLEMENT · 60 CAPSULES</p>

  <section class="facts">
    <h2>Supplement Facts</h2>
    <p>Serving Size: 2 Capsules</p>
    <p>Servings Per Container: 30</p>
    <div class="rule"></div>
    <div class="amount"><span>Amount Per Serving</span><span>% Daily Value</span></div>
    <div class="rule thin"></div>
    <p class="formula">VE-Rx™ Proprietary Formula 1,560 mg †</p>
    <p class="ingredients">Horny Goat Weed (herb powder), Maca (herb powder), Macuna Pruriens (L-Dopa), Polypodium Vulgare (herb powder), Yohimbe Bark (herb powder), Saw Palmetto (herb powder), Muira Puama (herb powder), Arginine (L-Arginine hydrochloride), Panax Ginseng (herb powder).</p>
    <div class="rule"></div>
    <p class="dv">† % Daily Value not established</p>
  </section>
  <p class="other"><span>OTHER INGREDIENTS:</span> Gelatin, Magnesium Stearate, and Calcium Carbonate.</p>
</main>
</body>
</html>
```